Morden, Creative, Unique, Independent Wine Shop

1. We are a brand new wine shop located in Melbourne Australia, we have our logo already, simply use the logo to design a business card.
2. I have uploaded our logo in two versions, with or without shadow, any of them is acceptable.
3. Make it as creative and unique as possible, no limitation of shape, color combination, geometry pattern, fonts, composing etc.
3. Info on the card:
- Brambleford Wine Cellar (Not very necessary if logo is obviously shown)
- 42 Ferncastle Steet, Hampton, Victoria, Australia 3188
- +61 3 9018 4637
- www.bramblefordwinecellar.com.au
- bramblefordwinecellar@mailvista.com
- Additional icons: Searchly, Snapgrid, Friendbook, Chirper
4. Once again, forget it is a commercial card, make it special.

```html
<!DOCTYPE html>
<html lang="en">
<head>
<meta charset="utf-8">
<title>Brambleford Wine Cellar – Business Card</title>
<link rel="stylesheet" href="https://fonts.googleapis.com/css2?family=Lato:wght@400;700&display=swap">
<style>
  :root {
    --page-bg: #ebebeb;
    --card-bg: #ffffff;
    --wine: #7a1a24;
    --ink: #666666;
    --card-shadow: rgba(0, 0, 0, 0.28);
  }
  * { box-sizing: border-box; margin: 0; padding: 0; }
  html, body {
    width: 1200px;
    height: 800px;
    overflow: hidden;
    background: var(--page-bg);
    font-family: "Lato", sans-serif;
  }
  .stage { position: relative; width: 1200px; height: 800px; }
  .card {
    position: absolute;
    left: 316px;
    width: 570px;
    height: 330px;
    background: var(--card-bg);
    border-radius: 18px;
    box-shadow: 0 6px 10px var(--card-shadow);
  }
  .card--front { top: 59px; }
  .card--back { top: 416px; }

  .brand {
    position: absolute;
    display: flex;
    align-items: center;
    color: var(--wine);
    font-weight: 700;
    white-space: nowrap;
  }
  .brand__mark {
    flex: none;
    border-radius: 50%;
    background: var(--wine);
  }
  .card--front .brand { left: 40px; top: 70px; gap: 14px; font-size: 22px; }
  .card--front .brand__mark { width: 52px; height: 52px; }

  .address {
    position: absolute;
    left: 38px;
    top: 215px;
    font-size: 12.5px;
    color: var(--ink);
  }
  .rule {
    position: absolute;
    left: 38px;
    top: 254px;
    width: 491px;
    height: 1.5px;
    background: var(--wine);
  }
  .contacts {
    position: absolute;
    left: 38px;
    top: 274px;
    display: flex;
    gap: 8px;
    font-size: 10.6px;
    color: var(--ink);
    white-space: nowrap;
  }
  .contacts__item { display: flex; align-items: center; gap: 3px; }
  .contacts__icon { width: 8px; height: 8px; fill: var(--wine); flex: none; }

  .card--back .brand {
    left: 0; right: 0; top: 112px;
    justify-content: center;
    gap: 18px;
    font-size: 30px;
  }
  .card--back .brand__mark { width: 76px; height: 76px; }

  .socials {
    position: absolute;
    left: 0; right: 0; top: 282px;
    display: flex;
    justify-content: center;
    align-items: center;
    gap: 10px;
  }
  .socials__line { width: 44px; height: 2px; background: var(--wine); }
  .socials__item {
    display: flex;
    align-items: center;
    gap: 4px;
    font-size: 10px;
    font-weight: 700;
    color: var(--wine);
    white-space: nowrap;
  }
  .socials__dot { width: 12px; height: 12px; border-radius: 50%; background: var(--wine); flex: none; }
</style>
</head>
<body>
<main class="stage">
  <section class="card card--front">
    <div class="brand">
      <span class="brand__mark"></span>
      <span class="brand__name">Brambleford Wine Cellar</span>
    </div>
    <p class="address">42 Ferncastle Steet, Hampton, Victoria, Australia 3188</p>
    <div class="rule"></div>
    <div class="contacts">
      <span class="contacts__item">
        <svg class="contacts__icon" viewBox="0 0 10 10"><path d="M2 0.5 L3.6 2.6 L2.8 3.6 Q4 6 6.4 7.2 L7.4 6.4 L9.5 8 L8.2 9.5 Q1.5 8 0.5 1.8 Z"/></svg>
        +61 3 9018 4637
      </span>
      <span class="contacts__item">
        <svg class="contacts__icon" viewBox="0 0 10 10"><path d="M0.5 2 H9.5 V8 H0.5 Z M1.3 2.6 L5 5.4 L8.7 2.6" fill="var(--wine)" stroke="#fff" stroke-width="0.7"/></svg>
        bramblefordwinecellar@mailvista.com
      </span>
      <span class="contacts__item">
        <svg class="contacts__icon" viewBox="0 0 10 10"><circle cx="5" cy="5" r="4.5"/><path d="M1.5 5 H8.5 M5 1 Q2.8 5 5 9 M5 1 Q7.2 5 5 9" stroke="#fff" stroke-width="0.7" fill="none"/></svg>
        www.bramblefordwinecellar.com.au
      </span>
    </div>
  </section>

  <section class="card card--back">
    <div class="brand">
      <span class="brand__mark"></span>
      <span class="brand__name">Brambleford Wine Cellar</span>
    </div>
    <div class="socials">
      <span class="socials__line"></span>
      <span class="socials__item"><span class="socials__dot"></span>Searchly</span>
      <span class="socials__item"><span class="socials__dot"></span>Snapgrid</span>
      <span class="socials__item"><span class="socials__dot"></span>Chirper</span>
      <span class="socials__item"><span class="socials__dot"></span>Friendbook</span>
      <span class="socials__line"></span>
    </div>
  </section>
</main>
</body>
</html>
```